Business Card Design Project

I am a Chiropractor that is looking for a new business card.  Our logo was slightly changed lately, therefore need a new, more professional look.
We are a modern, non-stuffy chiropractic office.  Want a contemporary look that will let people know this is not your typical doctors office.  Our logo is red, and contains the name of our business: realign.  The u in the logo is green, stressing the most important part of our business: "u"

Target Market(s)
moderate to upper income bracket, family friendly
www.realignspine-example.com
Gordon Pell
Family Chiropractor
314 Hollis Rd
Larkfield, ZZ 78999
555.555.0147 phone
555.555.0148 fax
Industry/Entity Type
Business
Requirements
Must have
- www.realignspine-example.com
Gordon Pell
Family Chiropractor
314 Hollis Rd
Larkfield, ZZ 78999
555.555.0147 phone
555.555.0148 fax

```html
<!DOCTYPE html>
<html lang="en">
<head>
<meta charset="utf-8">
<title>realign – Business Card</title>
<link href="https://fonts.googleapis.com/css2?family=Arimo:wght@400;700&display=swap" rel="stylesheet">
<style>
  :root {
    --page-bg: #ffffff;
    --card-bg: #ffffff;
    --brand-red: #ee3b33;
    --brand-green: #6bb443;
    --text-grey: #4a4a4a;
    --band-text: #ffffff;
  }
  * { margin: 0; padding: 0; box-sizing: border-box; }
  html, body {
    width: 1200px; height: 901px; overflow: hidden;
    background: var(--page-bg);
    font-family: "Arimo", Arial, sans-serif;
  }
  .card {
    position: absolute;
    left: 295px; width: 612px; height: 350px;
    background: var(--card-bg);
    box-shadow: 3px 4px 8px rgba(0,0,0,0.35);
    overflow: hidden;
  }
  .card--front { top: 62px; }
  .card--back { top: 496px; }

  .brand-name {
    position: absolute; left: 0; right: 0;
    text-align: center;
    color: var(--brand-red);
    font-weight: 400;
    letter-spacing: 1px;
    line-height: 1;
  }
  .card--front .brand-name { top: 135px; font-size: 66px; }
  .card--back .brand-name { top: 76px; font-size: 60px; }

  .footer-band { position: absolute; left: 0; bottom: 0; width: 612px; height: 50px; }
  .footer-band .band-red { fill: var(--brand-red); }
  .footer-band .band-green { fill: var(--brand-green); }
  .website {
    position: absolute; left: 0; right: 0; bottom: 13px;
    text-align: center; color: var(--band-text);
    font-size: 17px;
  }

  .person {
    position: absolute; right: 355px; top: 219px;
    text-align: right;
  }
  .person__name { color: var(--brand-green); font-weight: 700; font-size: 19px; line-height: 24px; }
  .person__title { color: var(--text-grey); font-size: 15px; line-height: 20px; }

  .divider { position: absolute; left: 304px; top: 202px; width: 2px; height: 88px; }

  .contact {
    position: absolute; left: 363px; top: 202px;
    color: var(--text-grey); font-size: 15px; line-height: 21px;
    list-style: none;
  }
  .contact__icon { width: 14px; height: 12px; margin-right: 6px; vertical-align: -1px; fill: var(--brand-green); }
</style>
</head>
<body>

<section class="card card--front">
  <p class="brand-name">realign</p>
  <svg class="footer-band" viewBox="0 0 612 50" aria-hidden="true">
    <path class="band-red" d="M10 50 Q306 -48 602 50 Z"/>
    <path class="band-green" d="M30 50 Q306 -30 582 50 Z"/>
  </svg>
  <p class="website">www.realignspine-example.com</p>
</section>

<section class="card card--back">
  <p class="brand-name">realign</p>

  <div class="person">
    <p class="person__name">Gordon Pell</p>
    <p class="person__title">Family Chiropractor</p>
  </div>

  <svg class="divider" viewBox="0 0 2 88" aria-hidden="true">
    <defs>
      <linearGradient id="divider-fade" x1="0" y1="0" x2="0" y2="1">
        <stop offset="0" stop-color="#ee3b33" stop-opacity="0"/>
        <stop offset="0.5" stop-color="#ee3b33"/>
        <stop offset="1" stop-color="#ee3b33" stop-opacity="0"/>
      </linearGradient>
    </defs>
    <rect width="2" height="88" fill="url(#divider-fade)"/>
  </svg>

  <ul class="contact">
    <li>314 Hollis Rd</li>
    <li>Larkfield, ZZ 78999</li>
    <li>
      <svg class="contact__icon" viewBox="0 0 14 12" aria-label="Phone" role="img">
        <path d="M1 4 Q7 -1 13 4 L11 5.5 L9.5 3.8 L4.5 3.8 L3 5.5 Z"/>
        <path d="M3 6 L11 6 L12.5 11.5 L1.5 11.5 Z"/>
      </svg>555.555.0147
    </li>
    <li>
      <svg class="contact__icon" viewBox="0 0 14 12" aria-label="Fax" role="img">
        <rect x="3.5" y="0" width="7" height="3.5"/>
        <rect x="0.5" y="4" width="13" height="5.5" rx="1"/>
        <rect x="3.5" y="8" width="7" height="4" fill="#fff" stroke="#6bb443" stroke-width="1.2"/>
      </svg>555.555.0148
    </li>
  </ul>

  <svg class="footer-band" viewBox="0 0 612 50" aria-hidden="true">
    <path class="band-red" d="M10 50 Q306 -48 602 50 Z"/>
    <path class="band-green" d="M30 50 Q306 -30 582 50 Z"/>
  </svg>
  <p class="website">www.realignspine-example.com</p>
</section>

</body>
</html>
```